web design needed for brivolent safety ltd

We need a web design for our new company. It is called Brivo Lent Safety Ltd and is a company based around a security/safety/info box specifically made for on construction sites, but could be used elsewhere. It is completely portable with a builtin alarm system with remote. There is a larger box and a smaller box (only have an image for this one at this stage, I will get better photos of the temp box soon, but this one will make a start).
This will be the standard box that is for sale, howver you can get upgrades that include a fire extinguisher, first aid kit, hand sanitizer, fire blanket.
Other features include a place for plans and safety info for the site, a hook attached to the back of the smaller box so it can be hung on the door. Both boxes are suitable for outside.
We would like the wesite to incorporate our logo and pictures of the box. I have attached our logo and an exaple of a mock box as the final box is still being made sothese photos will be swapped once we have it from the manufacturer.
We would like the following pages:
Home (possibly a picture of the box rotating, doesnt have to though?)
About us
Products
FAQ
Shopping cart
Contact us
We would like the style to be crisp, simple and not to busy.
Thanks
Updates
More photos of the box have been added. These are for the larger box.
Reason: we are happy to give people more time so have extended it by seven days
Target Market(s)
Builders mainly
Industry/Entity Type
Construction
Font styles to use
Other font styles liked:
- ERAS BOLD ITC
Look and feel
Each slider illustrates characteristics of the customer's brand and the style your logo design should communicate.

```html
<!DOCTYPE html>
<html lang="en">
<head>
<meta charset="utf-8">
<title>Brivolent Safety</title>
<link rel="stylesheet" href="https://fonts.googleapis.com/css2?family=Lato:ital,wght@0,300;0,400;0,700;0,900;1,400;1,700&display=swap">
<style>
:root{
  --blue:#1aa9d6;
  --ink:#333;
  --muted:#777;
  --line:#e2e2e2;
  --topbar:#f7f7f7;
  --hero:#fcf8f4;
  --band:#f5f5f5;
  --foot:#f1f1f1;
  --foot-base:#e4e4e4;
  --red:#d9232b;
  --gold:#e6b800;
  --green:#7dbb2e;
}
*{box-sizing:border-box;margin:0;padding:0}
html,body{width:847px;height:1200px;overflow:hidden}
body{position:relative;font-family:"Lato",sans-serif;color:var(--ink);background:#fff}
.abs{position:absolute}
ul{list-style:none}

.topbar{left:0;top:0;width:847px;height:33px;background:var(--topbar);border-bottom:1px solid var(--line);font-size:8px;color:#555}
.topbar span{position:absolute;top:12px}
.topbar .cart-count{top:10px;left:736px;font-size:12px;font-weight:900;color:#444}

.header{left:0;top:33px;width:847px;height:66px;border-bottom:1px solid var(--line)}
.brand{left:78px;top:46px;display:flex;align-items:center;gap:6px}
.brand-dot{width:22px;height:22px;border-radius:50%;background:var(--green)}
.brand-name{font-size:10px;font-weight:900;letter-spacing:.3px;color:#222}
.nav{top:52px;left:349px;display:flex;font-size:12.5px;font-style:italic;font-weight:700;color:#444}
.nav a{color:inherit;text-decoration:none;padding:0 11px;height:34px;line-height:34px}
.nav a.current{color:var(--blue);border:1px solid var(--blue);padding:0 14px;margin-right:0}

.hero{left:0;top:99px;width:847px;height:289px;background:var(--hero);border-bottom:1px solid var(--line)}
.hero-art{left:135px;top:120px;width:285px;height:230px;border-radius:6px;background:linear-gradient(135deg,#e9e4de 0%,#d8d2cb 45%,#f1ece6 100%)}
.hero-title{left:477px;top:152px;font-size:21px;font-weight:900;color:#222;letter-spacing:-.2px}
.hero-sub{left:477px;top:179px;font-size:16px;font-weight:700;color:#666}
.hero-list{left:479px;top:211px;width:230px;font-size:9px;font-weight:700;color:#333;line-height:12.5px}
.hero-list li{position:relative;padding-left:16px;margin-bottom:4px}
.hero-list svg{position:absolute;left:0;top:2px}
.shop-now{left:483px;top:326px;font-size:12px;font-weight:700;color:#333;display:flex;align-items:center;gap:8px}

.features{left:0;top:388px;width:847px;height:286px;background:var(--band);border-bottom:1px solid var(--line)}
.section-title{font-size:21px;font-weight:400;color:var(--blue)}
.box-art{border-radius:3px;background:linear-gradient(160deg,#e23b47,#b3141f)}
.feature h3{font-size:12px;font-weight:400;color:#222;margin-bottom:6px}
.feature p{font-size:8.6px;font-weight:300;color:#666;line-height:12.6px;width:170px;margin-bottom:6px}
.feature li{font-size:8.6px;font-weight:300;color:#666;line-height:14px;position:relative;padding-left:9px}
.feature li::before{content:"";position:absolute;left:0;top:5px;width:4px;height:4px;border-radius:50%;background:var(--blue)}
.btn{display:inline-block;border:1px solid #ccc;background:#fff;font-size:10px;font-weight:300;color:#555;padding:4px 11px;position:absolute}
.divider{left:440px;top:483px;width:1px;height:137px;background:#ddd}

.arrow-btn{width:26px;height:26px;border:1px solid #555;border-radius:50%;display:flex;align-items:center;justify-content:center}
.card{width:96px;height:114px;border:1px solid var(--line);background:#fff}
.card .thumb{position:absolute;left:18px;top:22px;width:58px;height:76px;border-radius:4px}
.view-tag{position:absolute;left:0;top:20px;width:71px;height:15px;background:var(--blue);color:#fff;font-size:9px;font-weight:700;padding:2px 8px}
.product h4{font-size:11.5px;font-weight:300;color:#555}
.price{font-size:8.6px;font-weight:300;color:var(--blue);margin-top:3px}
.price s{color:#666;margin-left:5px}
.stars{font-size:11px;color:var(--gold);letter-spacing:1px;margin-top:3px}
.stars .off{color:#bbb}
.add{position:relative;display:inline-block;margin-top:14px;border:1px solid #ccc;font-size:7.5px;font-weight:300;color:#666;padding:3px 5px}

.footer{left:0;top:1013px;width:847px;height:137px;background:var(--foot)}
.foot-col h5{font-size:12px;font-weight:300;color:#555;margin-bottom:8px}
.foot-col li{font-size:8.6px;font-weight:300;color:#666;line-height:14px;position:relative;padding-left:8px}
.foot-col li::before{content:"";position:absolute;left:0;top:5px;width:3px;height:3px;border-radius:50%;background:var(--blue)}
.foot-col li.active{color:var(--blue)}
.contact-row{display:flex;gap:8px;font-size:8.6px;font-weight:300;color:#666;line-height:13.5px;margin-bottom:8px}
.base{left:0;top:1150px;width:847px;height:50px;background:var(--foot-base);font-size:8px;color:#444}
.base span{position:absolute;top:21px}
</style>
</head>
<body>

<div class="abs topbar">
  <span style="left:76px">English ⌄</span>
  <span style="left:128px">Currency : USD ⌄</span>
  <span style="left:644px">Login ⌄</span>
  <svg class="abs" style="left:704px;top:9px" width="24" height="17" viewBox="0 0 24 17" fill="none" stroke="#1aa9d6" stroke-width="1.6"><path d="M1 2h4l3 10h12l2-7H7"/><circle cx="10" cy="15" r="1.3"/><circle cx="18" cy="15" r="1.3"/></svg>
  <span class="cart-count">0 item</span>
</div>

<header class="abs header"></header>
<div class="abs brand"><span class="brand-dot"></span><span class="brand-name">BRIVOLENT SAFETY</span></div>
<nav class="abs nav">
  <a class="current">Home</a><a>About us</a><a>Products</a><a>FAQ</a><a>Shopping cart</a><a>Contact us</a>
</nav>

<section class="abs hero"></section>
<div class="abs hero-art" role="img" aria-label="Safety products: fire extinguisher, safe box, laptop, first aid kit and sanitizer bottle"></div>
<h1 class="abs hero-title">BRIVOLENT SAFETY</h1>
<p class="abs hero-sub">Security/Safety/Info Box</p>
<ul class="abs hero-list">
  <li><svg width="10" height="8" viewBox="0 0 10 8" fill="none" stroke="#999"><path d="M1 1h8v4H4L2 7V5H1z"/></svg>Specifically Made For On Construction Sites</li>
  <li><svg width="10" height="8" viewBox="0 0 10 8" fill="none" stroke="#999"><path d="M1 1h8v4H4L2 7V5H1z"/></svg>It is Completely Portable With a Builtin Alarm System With Remote</li>
  <li><svg width="10" height="8" viewBox="0 0 10 8" fill="none" stroke="#999"><path d="M1 1h8v4H4L2 7V5H1z"/></svg>Also Could Be Used Elsewhere</li>
  <li><svg width="10" height="8" viewBox="0 0 10 8" fill="none" stroke="#999"><path d="M1 1h8v4H4L2 7V5H1z"/></svg>Place For Plans And Safety Info</li>
  <li><svg width="10" height="8" viewBox="0 0 10 8" fill="none" stroke="#999"><path d="M1 1h8v4H4L2 7V5H1z"/></svg>A Hook Aattached To The Back of The Smaller Box so it can be hung on the door</li>
</ul>
<div class="abs shop-now">Shop Now <svg width="26" height="8" viewBox="0 0 26 8" fill="none" stroke="#777" stroke-width="1.3"><path d="M0 4h24M20 1l4 3-4 3"/></svg></div>

<section class="abs features"></section>
<h2 class="abs section-title" style="left:93px;top:420px">Our Features</h2>
<div class="abs box-art" style="left:90px;top:483px;width:123px;height:65px" role="img" aria-label="Larger red safety box, open, with extinguisher"></div>
<div class="abs feature" style="left:225px;top:481px">
  <h3>Our Larger Box</h3>
  <p>Lorem Ipsum is simply dummy text of the printing and typesetting industry. Lorem Ipsum has been the industry's standard</p>
  <ul><li>Fire Extinguisher</li><li>First Aid Kit</li><li>Hand Sanitizer</li><li>Fire Blanket</li></ul>
</div>
<span class="btn" style="left:229px;top:622px">View More</span>
<div class="abs divider"></div>
<div class="abs box-art" style="left:459px;top:493px;width:93px;height:64px" role="img" aria-label="Smaller red safety box, closed"></div>
<div class="abs feature" style="left:565px;top:481px">
  <h3>Our Small Box</h3>
  <p>Other features include a place for plans and safety info for the site, a hook attached to the back of the smaller box so it can be hung on the door</p>
  <ul><li>Fire Extinguisher</li><li>First Aid Kit</li><li>Hand Sanitizer</li><li>Fire Blanket</li></ul>
</div>
<span class="btn" style="left:568px;top:622px">View More</span>

<h2 class="abs section-title" style="left:93px;top:686px">Onsale Products</h2>
<div class="abs arrow-btn" style="left:691px;top:683px"><svg width="12" height="8" viewBox="0 0 12 8" fill="none" stroke="#555"><path d="M12 4H1M4 1 1 4l3 3"/></svg></div>
<div class="abs arrow-btn" style="left:721px;top:683px"><svg width="12" height="8" viewBox="0 0 12 8" fill="none" stroke="#555"><path d="M0 4h11M8 1l3 3-3 3"/></svg></div>

<div class="abs card" style="left:93px;top:729px"><div class="thumb" style="background:linear-gradient(#e33,#a11)" role="img" aria-label="Red fire extinguisher"></div><span class="view-tag">View</span></div>
<div class="abs product" style="left:200px;top:734px"><h4>Fire Blanket</h4><p class="price">$120.00 <s>$180.0</s></p><p class="stars">★★<span class="off">★★★</span></p><span class="add">ADD TO CART</span></div>

<div class="abs card" style="left:319px;top:729px"><div class="thumb" style="left:17px;top:26px;width:62px;height:60px;background:linear-gradient(#ee3a3a,#b81c1c)" role="img" aria-label="Red security info box"></div></div>
<div class="abs product" style="left:426px;top:734px"><h4>Security Info Box</h4><p class="price">$130.00 <s>$180.00</s></p><p class="stars">★★<span class="off">★★★</span></p><span class="add">ADD TO CART</span></div>

<div class="abs card" style="left:559px;top:729px"><div class="thumb" style="left:15px;top:30px;width:66px;height:52px;background:linear-gradient(#f04040,#b51818)" role="img" aria-label="Red first aid box"></div></div>
<div class="abs product" style="left:666px;top:734px"><h4>First Aid Box</h4><p class="price">$130.00 <s>$180.00</s></p><p class="stars">★★<span class="off">★★★</span></p><span class="add">ADD TO CART</span></div>

<div class="abs card" style="left:93px;top:872px"><div class="thumb" style="background:linear-gradient(#6cc8f0,#2a8fd0)" role="img" aria-label="Blue hand sanitizer bottle"></div></div>
<div class="abs product" style="left:200px;top:877px"><h4>Hand Sanitizer</h4><p class="price">$130.00 <s>$180.00</s></p><p class="stars">★★<span class="off">★★★</span></p><span class="add">ADD TO CART</span></div>

<div class="abs card" style="left:319px;top:872px"><div class="thumb" style="left:30px;width:36px;background:linear-gradient(#e33,#a11)" role="img" aria-label="Red fire extinguisher"></div></div>
<div class="abs product" style="left:426px;top:877px"><h4>Fire Blanket</h4><p class="price">$130.00 <s>$180.00</s></p><p class="stars">★★<span class="off">★★★</span></p><span class="add">ADD TO CART</span></div>

<div class="abs card" style="left:559px;top:872px"><div class="thumb" style="left:32px;width:32px;background:linear-gradient(90deg,#888,#eee,#777)" role="img" aria-label="Silver fire extinguisher"></div></div>
<div class="abs product" style="left:666px;top:877px"><h4>Fire Blanket</h4><p class="price">$130.00 <s>$180.00</s></p><p class="stars">★★<span class="off">★★★</span></p><span class="add">ADD TO CART</span></div>

<footer class="abs footer"></footer>
<div class="abs foot-col" style="left:93px;top:1033px"><h5>Customer Support</h5><ul><li class="active">Customer services</li><li>Returns</li><li>Buy gift cards</li><li>Size charts</li><li>Site map</li></ul></div>
<div class="abs foot-col" style="left:251px;top:1033px"><h5>Learn More</h5><ul><li>Greening our stores, and products</li><li>Education discount</li><li>Stylist services (in-store only)</li><li>How to write a review</li></ul></div>
<div class="abs foot-col" style="left:468px;top:1033px"><h5>Company</h5><ul><li>About us</li><li>Contact us</li><li>Tems and returns</li><li>Privacy policy</li><li>News &amp; media</li></ul></div>
<div class="abs foot-col" style="left:616px;top:1033px;width:160px">
  <h5>Contact Us</h5>
  <div class="contact-row"><svg width="12" height="16" viewBox="0 0 12 16"><path d="M6 0a6 6 0 0 0-6 6c0 4 6 10 6 10s6-6 6-10a6 6 0 0 0-6-6z" fill="#1aa9d6"/><circle cx="6" cy="6" r="2" fill="#fff"/></svg><span>Lorem ipsum dolor sit amet, consectetur adipisicing elit, sed do</span></div>
  <div class="contact-row"><svg width="12" height="14" viewBox="0 0 12 14"><rect width="12" height="14" rx="1" fill="#1aa9d6"/><path d="M2 2l8 10M10 2 2 12" stroke="#fff"/></svg><span>+00.123.456.700</span></div>
  <div class="contact-row"><svg width="12" height="16" viewBox="0 0 12 16" fill="none" stroke="#1aa9d6" stroke-width="1.5"><rect x="1" y="1" width="10" height="14" rx="1.5"/><path d="M5 12.5h2"/></svg><span>Support @ Brivolent-Safety</span></div>
</div>

<div class="abs base">
  <span style="left:78px">Home - &nbsp;About us &nbsp;- Products - &nbsp;FAQ - Shopping cart &nbsp;- Contact us</span>
  <span style="left:598px">CopyRight 2014@Brivolent-Safety-Ltd.com</span>
</div>

</body>
</html>
```